Movie Showtimes Website needs an updated new look

Website = www.reelhourly.net

We want to update the look of our website. We want our website to look modern, trendy, something that was designed in 2018.

We don't need any HTML or CSS or web development. All we need is the graphical prototype, preferably in Photoshop with layers.

Most of our visitors use mobile devices. Our website is RESPONSIVE -- it is flexible to fit all screen sizes.

We will use this new logo (designed on ArtPitchly):
https://www.artpitchly.net/design/40527716

Thank you for your kind consideration.

Please find attached 3 PDF files with the current webpages:

1. Each city location has its own HOME PAGE like this:

https://www.reelhourly.net/ont/ottawa/

2. The most visited pages have movie SHOWTIMES and look like this:

https://www.reelhourly.net/theatres/filmhaus-brookmere-vip

MOVIE TITLE (poster + basic info + 4 buttons)
-- the type of the screening (ex. Regular, VUMAX, 3D, etc.)
-- individual days and showtimes

3. INFORMATION about movies:

https://www.reelhourly.net/movies/quiet-harbour-tides-2018

Thank you.

Target Market(s)

Canada and USA, target audience = ages 13-50

Industry/Entity Type

Movie

Number of Pages Required

3 page

Font styles to use
Sans Serif

Colors

Designer to choose colors to be used in the design.

Requirements
Must have
• - For the main body text (such as movie times, description, information) we prefer dark text on a light background.
• - We will use the new logo https://www.artpitchly.net/design/40527716 -- but the text Reel Hourly in the logo doesn't have to look exactly like that, it can be on the same line and have the same or different size
Should not have
• No more than 2 different fonts (ex. one font for headers and titles, another one for text)

```html
<!DOCTYPE html>
<html lang="en">
<head>
<meta charset="utf-8">
<title>Reel Hourly – Home</title>
<link href="https://fonts.googleapis.com/css2?family=PT+Sans:wght@400;700&family=PT+Sans+Narrow:wght@400;700&display=swap" rel="stylesheet">
<style>
:root{
  --blue:#3fa9f5;
  --blue-dark:#2a8fd8;
  --ink:#222;
  --text:#333;
  --muted:#777;
  --line:#d9d9d9;
  --card:#f1f1f1;
  --dark:#2b2b2b;
  --board:#efefef;
  --white:#fff;
  --sea-top:#7c9fb8;
  --sea-bottom:#2e4d66;
}
*{box-sizing:border-box;margin:0;padding:0}
html,body{width:1200px;height:3041px;overflow:hidden}
body{background:var(--board);font-family:"PT Sans",sans-serif;color:var(--text);position:relative}
.abs{position:absolute}
.page{position:absolute;left:36px;top:91px;width:1130px;height:2129px;background:var(--white);overflow:hidden;box-shadow:0 2px 10px rgba(0,0,0,.12)}

/* header */
.brand{position:absolute;display:flex;align-items:center;gap:8px;font-family:"PT Sans Narrow",sans-serif;font-weight:700;color:var(--ink);letter-spacing:1px}
.brand-dot{width:32px;height:32px;border-radius:50%;background:var(--blue)}
.header .brand{left:150px;top:10px;font-size:26px}
.search{left:494px;top:14px;width:340px;height:34px;border:1px solid #bbb;border-radius:17px;font-size:11px;padding:9px 16px;color:var(--ink)}
.search-btn{position:absolute;right:4px;top:4px;width:24px;height:24px;border-radius:50%;background:var(--dark)}
.login{left:862px;top:14px;width:114px;height:34px;border:1px solid #bbb;border-radius:17px;font-size:11px;font-weight:700;color:var(--blue);display:flex;align-items:center;justify-content:center;gap:8px}
.nav{left:151px;top:69px;width:825px;height:45px;background:var(--blue);border-radius:23px;display:flex;justify-content:space-around;align-items:center;z-index:3}
.nav span{color:#fff;font-size:11px;font-weight:700;display:flex;align-items:center;gap:6px}
.nav span i{display:inline-block;width:12px;height:12px;border:1.5px solid #fff;border-radius:50%}

/* hero */
.hero{left:0;top:114px;width:1130px;height:310px;background:linear-gradient(180deg,var(--sea-top),#5d7f99 40%,var(--sea-bottom))}
.hero-arrow{position:absolute;top:130px;width:38px;height:36px;background:#3a3a3a;color:#fff;font-size:18px;display:flex;align-items:center;justify-content:center}
.hero-poster{left:179px;top:171px;width:200px;height:266px;background:linear-gradient(160deg,#3f4b46,#1e2523);box-shadow:0 3px 10px rgba(0,0,0,.4);z-index:4}
.hero-title{left:386px;top:205px;width:266px;height:49px;background:#111;color:#fff;font-family:"PT Sans Narrow",sans-serif;font-size:34px;letter-spacing:2px;padding:4px 14px;z-index:4}
.hero-btns{left:379px;top:261px;display:flex;z-index:4}
.hero-btns div{height:40px;background:var(--blue);color:#fff;font-family:"PT Sans Narrow",sans-serif;font-weight:700;font-size:17px;display:flex;align-items:center;padding:0 14px}
.hero-btns .ic{background:var(--blue-dark);width:40px;justify-content:center;padding:0}

/* content card */
.content{left:151px;top:394px;width:825px;height:760px;background:#fff;box-shadow:0 0 10px rgba(0,0,0,.15)}
.section-title{position:absolute;left:0;width:100%;text-align:center;font-weight:700;font-size:18px;letter-spacing:1.5px;color:var(--ink)}
.slide-arrow{position:absolute;font-size:28px;color:var(--ink)}
.movie{position:absolute;width:380px;height:233px;background:var(--card);box-shadow:0 1px 4px rgba(0,0,0,.15)}
.movie .poster{position:absolute;left:8px;top:8px;width:160px;height:210px}
.movie h3{position:absolute;left:185px;top:24px;font-size:12px;font-weight:700;text-transform:uppercase;color:var(--ink)}
.movie .when{position:absolute;left:185px;top:50px;font-size:11px;color:var(--ink);display:flex;align-items:center;gap:6px}
.movie .when b{font-weight:700}
.movie .info{position:absolute;left:185px;top:80px;width:182px;height:70px;background:#fff;padding:7px 8px;font-size:10px;line-height:20px;color:var(--text)}
.movie p{position:absolute;left:185px;top:165px;width:182px;font-size:10px;line-height:16px;color:var(--ink)}
.buy{position:absolute;left:8px;top:170px;width:160px;text-align:center;color:#fff;font-size:10px;font-weight:700}
.tabs{position:absolute;width:380px;display:flex;justify-content:space-around;padding:0 30px}
.tabs span{font-size:9px;font-weight:700;color:var(--ink);border-bottom:2px solid var(--blue);padding:0 2px 4px;display:flex;align-items:center;gap:10px}
.tabs span i{width:10px;height:10px;border:1px solid #aaa;border-radius:50%}
.show-all{left:461px;top:1136px;width:203px;height:37px;background:var(--dark);border-radius:19px;color:#fff;font-size:10px;font-weight:700;display:flex;align-items:center;padding-left:20px;z-index:5}
.show-all i{position:absolute;right:3px;top:3px;width:31px;height:31px;border-radius:50%;background:#fff}

/* promotions */
.promo-ghost{background:linear-gradient(160deg,#e4e4e4,#cfcfcf);box-shadow:0 2px 8px rgba(0,0,0,.1)}
.promo-poster{left:434px;top:1294px;width:187px;height:285px;background:linear-gradient(180deg,#e9e1d2,#f2c9d3 55%,#f4b53f);box-shadow:0 3px 10px rgba(0,0,0,.25)}
.promo-panel{left:624px;top:1309px;width:280px;height:240px;background:var(--blue);color:#fff;padding:26px 14px}
.promo-panel h4{font-size:19px;font-weight:700;letter-spacing:1px}
.promo-panel h5{font-size:8px;font-weight:700;margin-top:8px}
.promo-panel p{font-size:10px;line-height:17px;margin-top:12px}
.socials{display:flex;gap:10px;margin-top:16px}
.socials i{width:32px;height:32px;border:1px solid rgba(255,255,255,.7)}
.dots{position:absolute;left:14px;bottom:12px;display:flex;gap:4px}
.dots i{width:5px;height:5px;border-radius:50%;background:#fff}
.plus{position:absolute;right:-8px;bottom:-8px;width:26px;height:26px;border-radius:50%;background:#222;color:#fff;font-size:16px;text-align:center;line-height:25px}

/* birthdays */
.bday-strip{left:0;top:1694px;width:1130px;height:70px;display:flex;gap:10px;padding:0 0 0 10px}
.bday{width:178px;height:70px;background:var(--dark);display:flex;align-items:center;gap:10px;padding:6px}
.bday .ph{width:52px;height:58px;background:linear-gradient(160deg,#9a7e6b,#4e3d33)}
.bday b{display:block;font-size:11px;color:#fff}
.bday small{font-size:8px;color:#ccc}

/* footer */
.footer{left:0;top:1780px;width:1130px;height:349px;background:var(--dark);color:#fff}
.f-col{position:absolute;top:28px;font-size:9px;line-height:21px;color:#ddd}
.f-col h6{font-size:10px;font-weight:700;color:#fff;margin-bottom:10px}
.footer .brand{left:452px;top:186px;color:#fff;font-size:28px}
.f-rule{position:absolute;top:206px;height:1px;background:#555;width:400px}
.f-social{position:absolute;left:484px;top:268px;display:flex;gap:14px}
.f-social i{width:28px;height:28px;border-radius:50%;background:#444}
.copy{position:absolute;top:318px;width:100%;text-align:center;font-size:9px;color:#ccc}

/* device view */
.dv-title{left:0;top:2298px;width:1200px;text-align:center;font-family:"PT Sans Narrow",sans-serif;font-size:56px;letter-spacing:22px;color:#111}
.dv-line{height:3px;background:#111}
.screen{position:absolute;background:#fff;overflow:hidden;box-shadow:0 2px 10px rgba(0,0,0,.15);border-radius:4px}
</style>
</head>
<body>

<main class="page">
  <header class="header">
    <div class="brand"><span class="brand-dot"></span>REEL HOURLY</div>
    <div class="abs search">Search<span class="search-btn"></span></div>
    <div class="abs login">
      <svg width="14" height="14" viewBox="0 0 14 14"><circle cx="6" cy="4" r="3" fill="#222"/><path d="M0 13c0-4 3-5 6-5s6 1 6 5z" fill="#222"/></svg>LOGIN</div>
  </header>

  <nav class="abs nav">
    <span>CINEMAS <i></i></span><span>MOVIES <i></i></span><span>TOP 10 <i></i></span><span>TRAILERS <i></i></span><span>UPCOMING <i></i></span><span>DVD <i></i></span><span>MORE <i></i></span>
  </nav>

  <section class="abs hero" role="img" aria-label="Wide photo of a calm sea under a hazy sky with a film strip running into the distance">
    <div class="hero-arrow" style="left:0">&#8592;</div>
    <div class="hero-arrow" style="right:0">&#8594;</div>
  </section>
  <div class="abs hero-poster" role="img" aria-label="Featured film poster, dim teal still"></div>
  <div class="abs hero-title">REEL HOURLY</div>
  <div class="abs hero-btns">
    <div>Choose Cinema</div><div class="ic"><svg width="20" height="16"><rect x="1" y="4" width="18" height="11" fill="#fff"/><path d="M1 4l4-3 4 3 4-3 4 3" stroke="#fff" fill="none"/></svg></div>
    <div>Choose Movie</div><div class="ic"><svg width="20" height="16"><circle cx="6" cy="5" r="4" fill="#fff"/><circle cx="14" cy="5" r="4" fill="#fff"/><rect x="2" y="8" width="14" height="7" fill="#fff"/></svg></div>
  </div>

  <section class="abs content">
    <h2 class="section-title" style="top:66px">NEW MOVIE THIS WEEK</h2>
    <span class="slide-arrow" style="left:-14px;top:160px">&#8249;</span>
    <span class="slide-arrow" style="right:-14px;top:160px">&#8250;</span>

    <article class="movie" style="left:23px;top:117px">
      <div class="poster" role="img" aria-label="Film still of three volleyball players in green jerseys" style="background:linear-gradient(160deg,#5b6f58,#2e3a30)"></div>
      <div class="buy">BUY TICKET</div>
      <h3>The Lantern Season</h3>
      <div class="when"><svg width="14" height="14"><rect x="1" y="2" width="12" height="11" fill="#222"/></svg><span><b>TODAY :</b> 1:50, 4:30, 7:25, 9:50</span></div>
      <div class="info">Year : 2018 &nbsp;| &nbsp;Run Time : 1h 41m<br>Company : Summitline Pictures<br>Directed By : Owen Patterly</div>
      <p>Based on the inspiring true story of Westbrook High's volleyball team...</p>
    </article>
    <div class="tabs" style="left:23px;top:364px"><span>TIMES <i></i></span><span>INFO <i></i></span><span>VIDEO <i></i></span><span>REVIEWS <i></i></span></div>

    <article class="movie" style="left:423px;top:117px">
      <div class="poster" role="img" aria-label="Portrait of a woman in a dark hat" style="background:linear-gradient(160deg,#6b5a4b,#2d3440)"></div>
      <h3>La Marchand</h3>
      <div class="when"><svg width="14" height="14"><rect x="1" y="2" width="12" height="11" fill="#222"/></svg><span><b>TODAY :</b> 1:15, 4:00, 6:45, 9:25</span></div>
      <div class="info">Year : 2018 &nbsp;| &nbsp;Run Time : 1h 43m<br>Company : Les Films Arvelle<br>Directed By : Luc Desrosiers</div>
      <p>This is the life story of Rose Vallée also known by her stage name of La Marchand...</p>
    </article>
    <div class="tabs" style="left:423px;top:364px"><span>TIMES <i></i></span><span>INFO <i></i></span><span>VIDEO <i></i></span><span>REVIEWS <i></i></span></div>

    <article class="movie" style="left:23px;top:420px">
      <div class="poster" role="img" aria-label="Two women seated on a park bench" style="background:linear-gradient(160deg,#7c9a5e,#3e4d33)"></div>
      <h3>Mistral</h3>
      <div class="when"><svg width="14" height="14"><rect x="1" y="2" width="12" height="11" fill="#222"/></svg><span><b>PLAYING TOMORROW :</b> 6:30</span></div>
      <div class="info">Year : 2017 &nbsp;| &nbsp;Run Time : 1h 31m<br>Company : Cedar Coast Pictures<br>Directed By : Claire Mondet</div>
      <p>Nora and Sam, a well-to-do American couple in romantic Paris...</p>
    </article>
    <div class="tabs" style="left:23px;top:667px"><span>TIMES <i></i></span><span>INFO <i></i></span><span>VIDEO <i></i></span><span>REVIEWS <i></i></span></div>

    <article class="movie" style="left:423px;top:420px">
      <div class="poster" role="img" aria-label="Misty grey lake with a long wooden bridge" style="background:linear-gradient(180deg,#c9c9cb,#6f6e73)"></div>
      <h3>Harrowmere Bay</h3>
      <div class="when"><svg width="14" height="14"><rect x="1" y="2" width="12" height="11" fill="#222"/></svg><span><b>TODAY :</b> 1:20, 4:10, 7:00, 9:45</span></div>
      <div class="info">Year : 2017 &nbsp;| &nbsp;Run Time : 1h 47m<br>Company : Brightway Studios<br>Directed By : Neil Harlan</div>
      <p>This suspenseful historical drama examines the infamous 1969...</p>
    </article>
    <div class="tabs" style="left:423px;top:667px"><span>TIMES <i></i></span><span>INFO <i></i></span><span>VIDEO <i></i></span><span>REVIEWS <i></i></span></div>
  </section>
  <div class="abs show-all">SHOW ALL PLAYING MOVIES<i></i></div>

  <h2 class="section-title" style="top:1230px">PROMOTIONS</h2>
  <div class="abs promo-ghost" style="left:224px;top:1313px;width:120px;height:246px;opacity:.5"></div>
  <div class="abs promo-ghost" style="left:264px;top:1302px;width:170px;height:268px;background:linear-gradient(160deg,#d8dcda,#8e9693)" role="img" aria-label="Faded film poster in the carousel"></div>
  <div class="abs promo-poster" role="img" aria-label="Comedy film poster: a woman in a pink suit above large yellow title lettering"></div>
  <div class="abs promo-panel">
    <h4>I FEEL BRAVE</h4>
    <h5>WIN FREE TICKETS TO THE OTTAWA ADVANCE SCREENING!</h5>
    <p>In I FEEL BRAVE an ordinary woman who struggles with feelings of insecurity and inadequacy on a daily basis wakes from a fall believing she is suddenly the most beautiful and capable...</p>
    <div class="socials"><i></i><i></i><i></i><i></i></div>
    <div class="dots"><i></i><i></i><i></i></div>
    <span class="plus">+</span>
  </div>

  <h2 class="section-title" style="top:1643px">HAPPY BIRTHDAY</h2>
  <div class="abs bday-strip">
    <div class="bday"><div class="ph" role="img" aria-label="Actor portrait"></div><div><b>Marcus Ellery</b><small>64 years old</small></div></div>
    <div class="bday"><div class="ph" role="img" aria-label="Actor portrait"></div><div><b>Marcus Ellery</b><small>64 years old</small></div></div>
    <div class="bday"><div class="ph" role="img" aria-label="Actor portrait"></div><div><b>Marcus Ellery</b><small>64 years old</small></div></div>
    <div class="bday"><div class="ph" role="img" aria-label="Actor portrait"></div><div><b>Marcus Ellery</b><small>64 years old</small></div></div>
    <div class="bday"><div class="ph" role="img" aria-label="Actor portrait"></div><div><b>Marcus Ellery</b><small>64 years old</small></div></div>
    <div class="bday"><div class="ph" role="img" aria-label="Actor portrait"></div><div><b>Marcus Ellery</b><small>64 years old</small></div></div>
  </div>

  <footer class="abs footer">
    <div class="f-col" style="left:151px"><h6>NAVIGATION</h6>Cinemas<br>Movies<br>Top 10<br>Trailers<br>Upcoming</div>
    <div class="f-col" style="left:302px;top:59px">DVD<br>More</div>
    <div class="f-col" style="left:453px"><h6>QUICK LINKS</h6>Site Map<br>Videos<br>Login<br>Search<br>Help</div>
    <div class="f-col" style="left:656px"><h6>TOP MOVIES</h6>Only the Echo<br>Dear, Theo<br>Letters from Rome<br>Iron Meridian<br>A Hollow Field</div>
    <div class="f-col" style="left:905px"><h6>VIDEOS</h6>Movie Trailers<br>Weekend Ticket</div>
    <span class="f-rule" style="left:0"></span><span class="f-rule" style="right:0"></span>
    <div class="brand"><span class="brand-dot"></span>REEL HOURLY</div>
    <div class="f-social"><i></i><i></i><i></i><i></i></div>
    <div class="copy">Copyright 2018 © reel hourly. All Rights Reserved.</div>
  </footer>
</main>

<div class="abs dv-line" style="left:190px;top:2300px;width:810px"></div>
<div class="abs dv-title">DEVICE VIEW</div>
<div class="abs dv-line" style="left:190px;top:2372px;width:810px"></div>

<!-- desktop screen -->
<div class="screen" style="left:210px;top:2430px;width:660px;height:400px">
  <div class="brand" style="left:40px;top:8px;font-size:16px"><span class="brand-dot" style="width:20px;height:20px"></span>REEL HOURLY</div>
  <div class="abs search" style="left:270px;top:10px;width:200px;height:22px;padding:4px 10px;font-size:8px">Search</div>
  <div class="abs login" style="left:490px;top:10px;width:70px;height:22px;font-size:8px">LOGIN</div>
  <div class="abs" style="left:40px;top:42px;width:580px;height:30px;background:var(--blue);border-radius:15px"></div>
  <div class="abs" style="left:0;top:72px;width:660px;height:255px;background:linear-gradient(180deg,var(--sea-top),var(--sea-bottom))" role="img" aria-label="Sea photo hero"></div>
  <div class="abs" style="left:40px;top:95px;width:150px;height:200px;background:linear-gradient(160deg,#3f4b46,#1e2523)" role="img" aria-label="Featured film poster"></div>
  <div class="abs" style="left:195px;top:130px;background:#111;color:#fff;font-family:'PT Sans Narrow',sans-serif;font-size:26px;padding:2px 10px;letter-spacing:1px">REEL HOURLY</div>
  <div class="abs" style="left:190px;top:172px;width:240px;height:28px;background:var(--blue)"></div>
  <div class="section-title" style="top:356px;font-size:15px">NEW MOVIE THIS WEEK</div>
</div>

<!-- tablet screen -->
<div class="screen" style="left:880px;top:2440px;width:250px;height:470px">
  <div class="brand" style="left:8px;top:10px;font-size:13px"><span class="brand-dot" style="width:16px;height:16px"></span>REEL HOURLY</div>
  <div class="abs" style="left:0;top:46px;width:250px;height:26px;background:var(--blue);color:#fff;font-size:10px;font-weight:700;padding:6px 10px">MENU</div>
  <div class="abs" style="left:0;top:72px;width:250px;height:398px;background:linear-gradient(180deg,var(--sea-top),var(--sea-bottom))" role="img" aria-label="Sea photo hero"></div>
  <div class="abs" style="left:10px;top:100px;width:110px;height:150px;background:linear-gradient(160deg,#3f4b46,#1e2523)" role="img" aria-label="Featured film poster"></div>
  <div class="abs" style="left:100px;top:195px;background:#111;color:#fff;font-family:'PT Sans Narrow',sans-serif;font-size:16px;padding:2px 8px">REEL HOURLY</div>
  <div class="abs" style="left:100px;top:225px;width:140px;height:22px;background:var(--blue);color:#fff;font-size:9px;font-weight:700;padding:5px 8px">Choose Cinema</div>
  <div class="abs" style="left:100px;top:250px;width:140px;height:22px;background:var(--blue);color:#fff;font-size:9px;font-weight:700;padding:5px 8px">Choose Movie</div>
</div>

<!-- mobile screen -->
<div class="screen" style="left:80px;top:2740px;width:110px;height:210px">
  <div class="brand" style="left:5px;top:6px;font-size:8px;gap:3px"><span class="brand-dot" style="width:10px;height:10px"></span>REEL HOURLY</div>
  <div class="abs" style="left:0;top:26px;width:110px;height:14px;background:var(--blue);color:#fff;font-size:6px;font-weight:700;padding:3px 5px">MENU</div>
  <div class="abs" style="left:0;top:40px;width:110px;height:170px;background:linear-gradient(180deg,var(--sea-top),var(--sea-bottom))" role="img" aria-label="Sea photo hero"></div>
  <div class="abs" style="left:5px;top:50px;width:50px;height:70px;background:linear-gradient(160deg,#3f4b46,#1e2523)" role="img" aria-label="Featured film poster"></div>
  <div class="abs" style="left:58px;top:70px;background:#111;color:#fff;font-size:6px;padding:2px 4px;line-height:8px">REEL<br>HOURLY</div>
</div>

</body>
</html>
```